IT Company Business Card design

Brisk Loop is a new computer solutions business focusing on setting up servers and computer systems for small to medium sized businesses.

A business client will either request a solution, or support for a current system and we will turn up on site to provide these services.

We are bast in Christchurch, New Zealand.

We are looking for unique business card's that stand out and show off the business in a professional light.

Open to all idea's etc.

Industry/Entity Type

Computer

Requirements
Must have
• Business Logo (AI file attached)
Employee Name
Business title
Business landline number
Cell phone number
Email
Web URL
Nice to have
• Could be nice to have some keywords (possibly on the back) such as:

Business IT solutions
Network installations
Phone solutions
Server management
Software diagnostics

The above is not needed, just an idea.

```html
<!DOCTYPE html>
<html lang="en">
<head>
<meta charset="utf-8">
<title>Brisk Loop – Business Card</title>
<link rel="stylesheet" href="https://fonts.googleapis.com/css2?family=Questrial&family=Ubuntu:wght@400&display=swap">
<style>
  :root {
    --page-bg: #4b4f55;
    --card-bg: #dcdedf;
    --navy: #2b4288;
    --sky: #2490d0;
    --ink: #121212;
    --steel: #8e9092;
    --light-grey: #cfd0d2;
    --orange: #ee7a1f;
    --white: #ffffff;
    --icon-bg: #1f3a66;
    --social-grey: #7a7a7a;
  }
  * { margin: 0; padding: 0; box-sizing: border-box; }
  html, body {
    width: 1200px; height: 1000px; overflow: hidden;
    background: var(--page-bg);
  }
  .card {
    position: absolute; left: 152px; top: 225px;
    width: 900px; height: 540px;
    background: var(--card-bg);
    overflow: hidden;
  }
  .brand-mark {
    position: absolute; left: 118px; top: 52px;
    width: 196px; height: 196px; border-radius: 50%;
    background: var(--sky);
  }
  .brand-divider {
    position: absolute; left: 339px; top: 58px;
    width: 4px; height: 197px;
    background: linear-gradient(#ffffff, #9a9a9a, #ffffff);
  }
  .brand-name {
    position: absolute; left: 366px; top: 116px;
    font-family: "Questrial", sans-serif;
    font-size: 66px; letter-spacing: 6px;
    color: var(--ink); line-height: 1; white-space: nowrap;
  }
  .person-band {
    position: absolute; left: 0; top: 265px;
    width: 398px; height: 140px; background: var(--navy);
  }
  .person-name {
    position: absolute; left: 51px; top: 48px;
    font-family: "Questrial", sans-serif; font-size: 36px;
    color: var(--light-grey); line-height: 1;
  }
  .person-title {
    position: absolute; left: 51px; top: 88px;
    font-family: "Questrial", sans-serif; font-size: 20px;
    color: var(--orange); line-height: 1;
  }
  .contact-band {
    position: absolute; left: 403px; top: 265px;
    width: 497px; height: 140px; background: var(--sky);
  }
  .band-joint {
    position: absolute; left: 378px; top: 315px;
    width: 44px; height: 44px; border-radius: 50%;
    background: var(--steel); border: 3px solid var(--light-grey);
  }
  .contact-list {
    position: absolute; left: 40px; top: 18px; list-style: none;
    font-family: "Ubuntu", sans-serif; font-size: 19px;
    color: var(--white);
  }
  .contact-list li {
    display: flex; align-items: center; height: 28.5px;
  }
  .contact-list svg {
    width: 21px; height: 21px; margin-right: 8px; flex: none;
  }
  .rule {
    position: absolute; left: 0; top: 405px;
    width: 900px; height: 6px; background: var(--steel);
  }
  .footer-bar {
    position: absolute; left: 0; top: 411px;
    width: 900px; height: 27px; background: var(--ink);
    font-family: "Ubuntu", sans-serif; font-size: 18px;
    color: var(--light-grey);
  }
  .web-address { position: absolute; left: 51px; top: 3px; }
  .footer-divider {
    position: absolute; left: 627px; top: 0;
    width: 4px; height: 27px; background: var(--steel);
  }
  .follow { position: absolute; left: 648px; top: 3px; }
  .social-slot {
    position: absolute; top: 3px;
    width: 22px; height: 22px; border-radius: 3px;
    background: var(--social-grey);
  }
  .social-slot.first { left: 782px; }
  .social-slot.second { left: 809px; }
</style>
</head>
<body>
  <main class="card">
    <div class="brand-mark"></div>
    <div class="brand-divider"></div>
    <div class="brand-name">BRISK LOOP</div>

    <section class="person-band">
      <div class="person-name">Aaron Vell</div>
      <div class="person-title">IT Professional</div>
    </section>

    <section class="contact-band">
      <ul class="contact-list">
        <li>
          <svg viewBox="0 0 21 21"><rect width="21" height="21" rx="3" fill="var(--icon-bg)"/><path d="M4 11 L10.5 4.5 L17 11 L15 11 L15 16.5 L12 16.5 L12 12.5 L9 12.5 L9 16.5 L6 16.5 L6 11 Z" fill="#fff"/></svg>
          Harper Lane, Easton EA4 7RT
        </li>
        <li>
          <svg viewBox="0 0 21 21"><rect width="21" height="21" rx="3" fill="var(--icon-bg)"/><rect x="6.5" y="3" width="8" height="15" rx="1.5" fill="#fff"/><rect x="8" y="5" width="5" height="6" fill="var(--icon-bg)"/><circle cx="10.5" cy="15" r="1" fill="var(--icon-bg)"/></svg>
          0800 555 0142
        </li>
        <li>
          <svg viewBox="0 0 21 21"><rect width="21" height="21" rx="3" fill="var(--icon-bg)"/><rect x="7" y="3.5" width="7" height="5" fill="#fff"/><rect x="3.5" y="9" width="14" height="6" rx="1" fill="#fff"/><rect x="6" y="14" width="9" height="3.5" fill="#fff"/></svg>
          987-654-321
        </li>
        <li>
          <svg viewBox="0 0 21 21"><rect width="21" height="21" rx="3" fill="var(--icon-bg)"/><rect x="3.5" y="6" width="14" height="9.5" fill="#fff"/><path d="M3.5 6 L10.5 11.5 L17.5 6" fill="none" stroke="var(--icon-bg)" stroke-width="1.3"/></svg>
          email@brisk-loop.com
        </li>
      </ul>
    </section>

    <div class="band-joint"></div>
    <div class="rule"></div>

    <footer class="footer-bar">
      <span class="web-address">www.brisk-loop.com</span>
      <div class="footer-divider"></div>
      <span class="follow">follow us on:</span>
      <span class="social-slot first"></span>
      <span class="social-slot second"></span>
    </footer>
  </main>
</body>
</html>
```